Cobalt Field Services website design

We want to create a Sports turf website for our business Cobalt Field Services - we do sports turf management on sports fields around the Mackay region soccer rugby league softball fields etc from full turf management plans and maintenance to just supply and apply of turf management products and just supply of products with program we also do grounds facility maintenance at council facility's and grounds that require a higher level of care - we will up load our logos and fonts etc to assist with the colour pallet for the website - we will have to have a landing page a shop page with tabs a gallery tab along with a grants initiative and our northreach finest green tab also - our font for the txt is called ethnocentric
Updates

how do we open time for people to submit we have no one submitted

Industry/Entity Type

Turf

Coding

Coded - Design and coding required

Number of Pages Required

5+ page

Font styles to use
Other font styles liked:
• ethnocentric

Requirements
Must have
• I have mentioned some waffle in the description that should assist
Should not have
• anything not related

```html
<!DOCTYPE html>
<html lang="en">
<head>
<meta charset="utf-8">
<title>Cobalt Field Services</title>
<link href="https://fonts.googleapis.com/css2?family=Inter:wght@300;400;500;600;700&display=swap" rel="stylesheet">
<style>
:root{
  --green-deep:#1f4a12;
  --green-bright:#4caf50;
  --green-soft:#7cad62;
  --green-cta:#1c3a0c;
  --navy:#141b2d;
  --ink:#1b1f24;
  --grey:#5f6670;
  --mist:#f7f9fa;
  --line:#e4e7ea;
  --white:#ffffff;
  --black:#000000;
}
*{box-sizing:border-box;margin:0;padding:0}
html,body{width:1200px;height:1200px;overflow:hidden;background:var(--white)}
body{font-family:"Inter",sans-serif;color:var(--ink)}
.page{position:absolute;left:450px;top:0;width:980px;height:3840px;transform:scale(.3125);transform-origin:0 0;overflow:hidden;background:var(--white);outline:3px solid var(--line)}
section,header,footer{position:relative;width:980px}
.wrap{padding:0 70px}
.title{font-weight:400;font-size:25px;letter-spacing:2.5px;text-transform:uppercase;color:var(--green-deep);text-align:center;padding-top:52px}
.lead{font-size:13px;line-height:20px;color:var(--grey);text-align:center;width:500px;margin:12px auto 0}
.btn{display:inline-flex;align-items:center;gap:7px;height:32px;padding:0 22px;border-radius:3px;font-size:10px;font-weight:500;color:var(--white);white-space:nowrap}
.btn svg{width:10px;height:10px}
.center{text-align:center}
.photo{display:block}

/* nav */
.nav{height:54px;display:flex;align-items:center;justify-content:space-between;padding:0 70px 0 82px;border-bottom:1px solid var(--line)}
.brand{font-size:17px;font-weight:700;letter-spacing:1px;color:var(--green-deep)}
.menu{display:flex;align-items:center;gap:22px;font-size:11px;color:var(--ink)}
.menu .active{color:var(--green-deep);font-weight:600;border-bottom:2px solid var(--green-bright);padding-bottom:4px}
.menu .btn{height:28px;padding:0 16px;background:var(--green-bright);font-weight:600}

/* hero */
.hero{height:490px;background:linear-gradient(180deg,#0e1a22 0%,#1d3320 38%,#2f6b22 62%,#3f8a2a 100%)}
.hero-text{position:absolute;left:70px;top:106px;width:520px}
.hero h1{font-weight:400;font-size:41px;line-height:51px;letter-spacing:1px;color:var(--white);text-transform:uppercase}
.hero h1 span{color:#6fbd57}
.hero p{margin-top:20px;font-size:13px;line-height:22px;color:#e8eee8;width:500px}
.hero .actions{margin-top:26px;display:flex;gap:10px}
.hero .btn{height:38px;padding:0 22px}
.btn-fill{background:var(--green-bright)}
.btn-outline{border:2px solid var(--white);background:transparent}

/* services */
.services{height:490px;background:var(--mist)}
.cards-3{display:flex;gap:21px;margin-top:48px}
.svc{width:266px;height:262px;background:var(--white);border-radius:6px;box-shadow:0 2px 10px rgba(0,0,0,.12);padding:22px}
.svc .ico{width:42px;height:42px;border-radius:4px;background:var(--green-deep);display:flex;align-items:center;justify-content:center}
.svc .ico svg{width:16px;height:16px}
.svc h3{margin-top:18px;font-size:15px;font-weight:700;color:var(--green-deep)}
.svc p{margin-top:12px;font-size:10px;line-height:16px;color:var(--grey)}
.ticks{margin-top:12px;list-style:none}
.ticks li{font-size:10px;color:var(--grey);display:flex;align-items:center;gap:6px;height:22px}
.ticks svg{width:10px;height:10px}

/* shop */
.shop{height:530px;background:var(--white)}
.cards-4{display:flex;gap:16px;margin-top:48px}
.product{width:198px;height:236px;background:var(--mist);border-radius:6px;padding:16px}
.product .photo{width:166px;height:130px;border-radius:2px}
.product h4{margin-top:12px;font-size:10px;font-weight:700}
.product p{margin-top:8px;font-size:9px;color:var(--grey)}
.product .price{margin-top:12px;font-size:10px;font-weight:700;color:var(--green-deep)}
.shop .more{margin-top:30px}
.btn-dark{background:var(--green-deep)}

/* gallery */
.gallery{height:452px;background:var(--navy)}
.gallery .title{color:var(--white)}
.gallery .lead{color:#c8ccd4}
.tiles{display:flex;gap:16px;margin-top:42px}
.tiles .photo{width:268px;height:174px;border-radius:3px}
.gallery .more{margin-top:34px}
.btn-ghost{border:2px solid var(--green-soft);color:#b9d4ad;background:transparent;height:34px}

/* work */
.work{height:540px;background:var(--mist)}
.cards-work{display:flex;gap:16px;margin-top:42px;align-items:flex-start}
.job{width:268px;background:var(--white);border-radius:4px;box-shadow:0 2px 10px rgba(0,0,0,.12)}
.job .photo{width:268px;height:174px;border-radius:4px 4px 0 0}
.job .body{padding:16px 16px 18px}
.job h4{font-size:13px;font-weight:700;color:var(--green-deep)}
.job p{margin-top:8px;font-size:10px;line-height:15px;color:var(--grey)}
.work .more{margin-top:32px}

/* grants */
.grants{height:370px;background:var(--green-soft)}
.split{position:absolute;top:0;left:70px;width:840px;height:100%}
.grants .copy{position:absolute;left:0;top:54px;width:380px}
.side-title{font-weight:400;font-size:25px;letter-spacing:2.5px;text-transform:uppercase;color:var(--green-deep);white-space:nowrap}
.grants .copy p{margin-top:16px;font-size:11px;line-height:19px;color:#1e3314}
.dots{list-style:none;margin-top:14px}
.dots li{display:flex;align-items:center;gap:8px;height:25px;font-size:10px;color:#1e3314}
.dots i{width:9px;height:9px;border-radius:50%;background:var(--green-deep);display:block}
.grants .btn{margin-top:18px;background:var(--green-cta)}
.grants .photo{position:absolute;left:436px;top:54px;width:404px;height:262px;border-radius:3px}

/* finest green */
.best{height:400px;background:var(--white)}
.best .photo{position:absolute;left:0;top:68px;width:404px;height:262px;border-radius:4px}
.best .copy{position:absolute;left:436px;top:54px;width:404px}
.best .side-title{font-size:22px;letter-spacing:2px}
.best .copy>p{margin-top:14px;font-size:11px;line-height:19px;color:var(--grey)}
.perks{list-style:none;margin-top:14px}
.perks li{display:flex;gap:8px;margin-bottom:12px}
.perks svg{width:11px;height:11px;margin-top:2px;flex:none}
.perks b{display:block;font-size:10px;font-weight:600;color:var(--green-deep)}
.perks span{display:block;margin-top:3px;font-size:9px;color:var(--grey)}
.best .btn{margin-top:4px;background:var(--green-deep)}

/* cta */
.cta{height:254px;background:var(--green-cta)}
.cta .title{color:var(--white)}
.cta .lead{color:#cfdcc6;width:460px}
.cta .actions{margin-top:22px;display:flex;justify-content:center;gap:10px}
.cta .btn{height:40px}
.cta .btn-fill{background:var(--green-soft)}
.cta .btn-outline{border-color:var(--green-soft)}

/* footer */
.foot{height:260px;background:var(--black);color:#b4b8bd}
.cols{position:absolute;left:70px;top:44px;display:flex}
.col{width:216px}
.foot-brand{display:flex;align-items:center;gap:10px}
.foot-brand i{width:28px;height:28px;background:var(--green-deep);border-radius:3px;display:block}
.foot-brand b{font-size:13px;font-weight:400;letter-spacing:2px;color:var(--white)}
.foot-brand small{display:block;font-size:8px;letter-spacing:1px;color:var(--green-soft);margin-top:3px}
.col p{margin-top:20px;font-size:10px;line-height:16px;width:200px}
.social{display:flex;gap:10px;margin-top:14px}
.social i{width:9px;height:9px;border-radius:50%;background:var(--green-soft);display:block}
.col h5{font-size:10px;font-weight:600;color:var(--white)}
.col ul{list-style:none;margin-top:14px}
.col li{font-size:10px;height:22px;display:flex;align-items:center;gap:8px}
.col li svg{width:10px;height:10px}
.rule{position:absolute;left:70px;top:200px;width:840px;height:1px;background:#222}
.copyright{position:absolute;left:0;top:228px;width:980px;text-align:center;font-size:9px;color:#8a8f95}
</style>
</head>
<body>
<div class="page">

  <header class="nav">
    <div class="brand">COBALT FIELD SERVICES</div>
    <nav class="menu">
      <span class="active">Home</span><span>Services</span><span>Shop</span><span>Gallery</span><span>Grants</span><span>Northreach Finest</span>
      <span class="btn">Get Quote</span>
    </nav>
  </header>

  <section class="hero" role="img" aria-label="Floodlit stadium with a green sports field at night">
    <div class="hero-text">
      <h1>Premium Turf<br><span>Management</span> For<br>Mackay</h1>
      <p>Professional sports turf management services for clubs, councils, and commercial properties. Delivering championship-quality fields across Mackay and surrounding regions.</p>
      <div class="actions">
        <span class="btn btn-fill"><svg viewBox="0 0 10 10"><path d="M2 1l2 2-1 1.2c.6 1.2 1.6 2.2 2.8 2.8L7 6l2 2-1.2 1.2C4.5 9 1 5.5.8 2.2z" fill="#fff"/></svg>Get Free Assessment</span>
        <span class="btn btn-outline"><svg viewBox="0 0 10 10"><path d="M2 1l7 4-7 4z" fill="#fff"/></svg>View Our Work</span>
      </div>
    </div>
  </section>

  <section class="services wrap">
    <h2 class="title">Our Services</h2>
    <p class="lead">Comprehensive turf management solutions designed for professional sports facilities, councils, and commercial properties throughout Mackay.</p>
    <div class="cards-3">
      <div class="svc">
        <div class="ico"><svg viewBox="0 0 16 16"><circle cx="4" cy="4" r="2.2" fill="none" stroke="#fff" stroke-width="1.5"/><circle cx="4" cy="12" r="2.2" fill="none" stroke="#fff" stroke-width="1.5"/><path d="M6 5.5l8 7M6 10.5l8-7" stroke="#fff" stroke-width="1.5"/></svg></div>
        <h3>Field Maintenance</h3>
        <p>Regular mowing, line marking, and surface preparation for optimal playing conditions.</p>
        <ul class="ticks">
          <li><svg viewBox="0 0 10 10"><path d="M1 5l3 3 5-6" fill="none" stroke="#1f4a12" stroke-width="1.6"/></svg>Weekly maintenance schedules</li>
          <li><svg viewBox="0 0 10 10"><path d="M1 5l3 3 5-6" fill="none" stroke="#1f4a12" stroke-width="1.6"/></svg>Professional line marking</li>
          <li><svg viewBox="0 0 10 10"><path d="M1 5l3 3 5-6" fill="none" stroke="#1f4a12" stroke-width="1.6"/></svg>Surface leveling</li>
        </ul>
      </div>
      <div class="svc">
        <div class="ico"><svg viewBox="0 0 16 16"><path d="M8 2C6 6 4.5 8 4.5 10a3.5 3.5 0 007 0C11.5 8 10 6 8 2z" fill="#fff"/></svg></div>
        <h3>Irrigation Systems</h3>
        <p>Design, installation, and maintenance of efficient irrigation systems for optimal turf health.</p>
        <ul class="ticks">
          <li><svg viewBox="0 0 10 10"><path d="M1 5l3 3 5-6" fill="none" stroke="#1f4a12" stroke-width="1.6"/></svg>Smart irrigation design</li>
          <li><svg viewBox="0 0 10 10"><path d="M1 5l3 3 5-6" fill="none" stroke="#1f4a12" stroke-width="1.6"/></svg>Water-efficient systems</li>
          <li><svg viewBox="0 0 10 10"><path d="M1 5l3 3 5-6" fill="none" stroke="#1f4a12" stroke-width="1.6"/></svg>24/7 monitoring</li>
        </ul>
      </div>
      <div class="svc">
        <div class="ico"><svg viewBox="0 0 16 16"><path d="M8 14V8M8 8C8 5 6 3 3 3c0 3 2 5 5 5zM8 8c0-3 2-5 5-5 0 3-2 5-5 5z" fill="#fff" stroke="#fff" stroke-width="1.2"/></svg></div>
        <h3>Turf Installation</h3>
        <p>Premium turf varieties selected and installed for maximum durability and performance.</p>
        <ul class="ticks">
          <li><svg viewBox="0 0 10 10"><path d="M1 5l3 3 5-6" fill="none" stroke="#1f4a12" stroke-width="1.6"/></svg>Quality turf varieties</li>
          <li><svg viewBox="0 0 10 10"><path d="M1 5l3 3 5-6" fill="none" stroke="#1f4a12" stroke-width="1.6"/></svg>Professional installation</li>
          <li><svg viewBox="0 0 10 10"><path d="M1 5l3 3 5-6" fill="none" stroke="#1f4a12" stroke-width="1.6"/></svg>Establishment guarantee</li>
        </ul>
      </div>
    </div>
  </section>

  <section class="shop wrap">
    <h2 class="title">Turf Shop</h2>
    <p class="lead" style="width:390px">Premium turf products and equipment for professionals and enthusiasts</p>
    <div class="cards-4">
      <div class="product">
        <div class="photo" role="img" aria-label="Bags of turf seed on grass" style="background:linear-gradient(180deg,#4c8a34,#9a6a3a)"></div>
        <h4>Premium Seeds</h4><p>Professional grade turf seeds</p><div class="price">From $45</div>
      </div>
      <div class="product">
        <div class="photo" role="img" aria-label="Fertiliser packs" style="background:linear-gradient(135deg,#d9924a,#6aa83e)"></div>
        <h4>Fertilizers</h4><p>Specialized turf nutrition</p><div class="price">From $35</div>
      </div>
      <div class="product">
        <div class="photo" role="img" aria-label="Lawn mower on grass" style="background:linear-gradient(180deg,#4d8a34,#5e7a30)"></div>
        <h4>Tools &amp; Equipment</h4><p>Professional maintenance tools</p><div class="price">From $125</div>
      </div>
      <div class="product">
        <div class="photo" role="img" aria-label="Sprinkler watering a lawn" style="background:linear-gradient(180deg,#a8c9b8,#4f9a34)"></div>
        <h4>Irrigation</h4><p>Smart watering solutions</p><div class="price">From $200</div>
      </div>
    </div>
    <div class="center more"><span class="btn btn-dark">View All Products</span></div>
  </section>

  <section class="gallery wrap">
    <h2 class="title">Project Gallery</h2>
    <p class="lead">Showcasing our premium turf management projects across Mackay</p>
    <div class="tiles">
      <div class="photo" role="img" aria-label="Close view of marked turf" style="background:linear-gradient(135deg,#2f6f24,#5a9e42)"></div>
      <div class="photo" role="img" aria-label="Aerial view of a soccer pitch" style="background:linear-gradient(135deg,#4fa32c,#72c23a)"></div>
      <div class="photo" role="img" aria-label="Marked sports field surface" style="background:linear-gradient(135deg,#357a28,#5aa03e)"></div>
    </div>
    <div class="center more"><span class="btn btn-ghost">View Full Gallery</span></div>
  </section>

  <section class="work wrap">
    <h2 class="title">Our Work</h2>
    <p class="lead">Championship-quality results across Mackay</p>
    <div class="cards-work">
      <div class="job">
        <div class="photo" role="img" aria-label="Football match on a maintained field" style="background:linear-gradient(180deg,#c9d3dc,#5f9a40)"></div>
        <div class="body"><h4>Eastside Football Club</h4><p>Complete field renovation and maintenance program</p></div>
      </div>
      <div class="job">
        <div class="photo" role="img" aria-label="Baseball diamond in a regional stadium" style="background:linear-gradient(180deg,#a9c7e2,#5a9a3a)"></div>
        <div class="body"><h4>Regional Sports Complex</h4><p>Multi-sport facility turf management</p></div>
      </div>
      <div class="job">
        <div class="photo" role="img" aria-label="Cricket ground with pavilion" style="background:linear-gradient(180deg,#dbe6ee,#5fa334)"></div>
        <div class="body"><h4>Cricket Grounds</h4><p>Specialized cricket pitch preparation</p></div>
      </div>
    </div>
    <div class="center more"><span class="btn btn-fill">View Full Gallery</span></div>
  </section>

  <section class="grants">
    <div class="split">
      <div class="copy">
        <h2 class="side-title">Grants Initiative</h2>
        <p>We help clubs and councils access government grants for turf improvement projects. Our expertise in grant applications has secured over $2M in funding for local sports facilities.</p>
        <ul class="dots">
          <li><i></i>Grant application assistance</li>
          <li><i></i>Project planning &amp; documentation</li>
          <li><i></i>Compliance management</li>
          <li><i></i>Post-grant project delivery</li>
        </ul>
        <span class="btn">Learn About Grants</span>
      </div>
      <div class="photo" role="img" aria-label="Group presenting a grant cheque on a sports oval" style="background:linear-gradient(180deg,#dde6ec,#4f7a3a)"></div>
    </div>
  </section>

  <section class="best">
    <div class="split">
      <div class="photo" role="img" aria-label="Award ribbon beside a lush residential lawn" style="background:linear-gradient(90deg,#1f6fe0 0%,#2a7ad0 40%,#3f8a2a 60%,#5aa83c 100%)"></div>
      <div class="copy">
        <h2 class="side-title">Northreach Finest Green</h2>
        <p>Join our exclusive program for residential lawn perfection. We bring professional-grade turf management to your home, creating the best lawns in Mackay.</p>
        <ul class="perks">
          <li><svg viewBox="0 0 10 10"><path d="M5 .5l1.4 3 3.1.3-2.4 2.1.7 3.1L5 7.4 2.2 9l.7-3.1L.5 3.8l3.1-.3z" fill="#1f4a12"/></svg><div><b>Premium Lawn Care</b><span>Weekly maintenance with professional equipment</span></div></li>
          <li><svg viewBox="0 0 10 10"><path d="M2.5 1h5v3a2.5 2.5 0 01-5 0zM4.2 6.4h1.6V8H7v1H3V8h1.2z" fill="#1f4a12"/></svg><div><b>Competition Entry</b><span>Annual best lawn competition with prizes</span></div></li>
          <li><svg viewBox="0 0 10 10"><path d="M1 9C1 4 4 1 9 1 9 6 6 9 1 9z" fill="#1f4a12"/></svg><div><b>Eco-Friendly</b><span>Sustainable practices for healthy lawns</span></div></li>
        </ul>
        <span class="btn">Join the Program</span>
      </div>
    </div>
  </section>

  <section class="cta">
    <h2 class="title">Ready to Transform Your Turf?</h2>
    <p class="lead">Get in touch with Mackay's premier turf management specialists for a free consultation and quote.</p>
    <div class="actions">
      <span class="btn btn-fill"><svg viewBox="0 0 10 10"><path d="M2 1l2 2-1 1.2c.6 1.2 1.6 2.2 2.8 2.8L7 6l2 2-1.2 1.2C4.5 9 1 5.5.8 2.2z" fill="#fff"/></svg>Call (07) 4000 0000</span>
      <span class="btn btn-outline"><svg viewBox="0 0 10 10"><rect x=".5" y="2" width="9" height="6" fill="#fff"/><path d="M.5 2l4.5 3.5L9.5 2" fill="none" stroke="#1c3a0c"/></svg>Email Us</span>
    </div>
  </section>

  <footer class="foot">
    <div class="cols">
      <div class="col">
        <div class="foot-brand"><i></i><div><b>COBALT FIELD</b><small>SERVICES</small></div></div>
        <p>Premium turf management services for sports facilities, councils, and residential properties across Mackay.</p>
        <div class="social"><i></i><i></i><i></i></div>
      </div>
      <div class="col"><h5>Services</h5><ul><li>Field Maintenance</li><li>Irrigation Systems</li><li>Turf Installation</li><li>Fertilization</li></ul></div>
      <div class="col"><h5>Programs</h5><ul><li>Grants Initiative</li><li>Finest Green Program</li><li>Club Partnerships</li><li>Council Services</li></ul></div>
      <div class="col"><h5>Contact</h5><ul>
        <li><svg viewBox="0 0 10 10"><path d="M2 1l2 2-1 1.2c.6 1.2 1.6 2.2 2.8 2.8L7 6l2 2-1.2 1.2C4.5 9 1 5.5.8 2.2z" fill="#b4b8bd"/></svg>(07) 4000 0000</li>
        <li><svg viewBox="0 0 10 10"><rect x=".5" y="2" width="9" height="6" fill="#b4b8bd"/><path d="M.5 2l4.5 3.5L9.5 2" fill="none" stroke="#000"/></svg>hello@cobaltfield.example</li>
        <li><svg viewBox="0 0 10 10"><path d="M5 9.5S1.5 6 1.5 4a3.5 3.5 0 017 0C8.5 6 5 9.5 5 9.5z" fill="#b4b8bd"/><circle cx="5" cy="4" r="1.2" fill="#000"/></svg>Mackay, Queensland</li>
      </ul></div>
    </div>
    <div class="rule"></div>
    <div class="copyright">© 2025 Cobalt Field Services. All rights reserved.</div>
  </footer>

</div>
</body>
</html>
```